TV Antenna Installation business needs a unique flyer

We need a simple but effective flyer design for our TV Aerial installation company based in Newcastle, NSW, Australia called Clearpeak TV & Aerial Svcs.
We are trying to target areas where there has been a new transmitter installed and most houses just require their aerial redirecting and tv's retuning.

Industry/Entity Type

Business

Requirements
Must have
• We would like the idea of a headline phrase such as " Poor TV reception……..now a thing from the past" or something similar & catchy.
Also "Did you know a new transmitter has been recently installed in your area, we can therefore now GUARANTEE 100% PERFECT PICTURE
Charges from only $95.
- Free 5 year warranty
- Free signal testing
- Free Onsite Quote
Phone 0452 736 205
Nice to have
• Other services include:

- New Installs
- Extra Points & repairs
- TV wall mounting/Home Cinema
- Pull down tall masts

Modern tv picture, see example uploaded

```html
<!DOCTYPE html>
<html lang="en">
<head>
<meta charset="utf-8">
<title>Clearpeak TV &amp; Aerial Svcs – Flyer</title>
<link rel="stylesheet" href="https://fonts.googleapis.com/css2?family=Arimo:wght@400;700&family=Oswald:wght@700&display=swap">
<style>
  :root {
    --red: #e3000f;
    --red-dark: #a8000b;
    --red-light: #ff3b3b;
    --white: #ffffff;
    --panel: #f4f4f4;
    --silver-dark: #8c8c8c;
    --ink: #111111;
    --photo-light: #d8d8d8;
    --photo-mid: #a9a9a9;
    --photo-dark: #4a4a4a;
  }
  * { margin: 0; padding: 0; box-sizing: border-box; }
  html, body { width: 851px; height: 1200px; overflow: hidden; background: var(--panel); }
  .flyer { position: relative; width: 851px; height: 1200px; overflow: hidden; font-family: "Arimo", Arial, sans-serif; }
  .flyer__shapes { position: absolute; inset: 0; }
  .phone {
    position: absolute; left: 28px; top: 12px; height: 62px;
    display: flex; align-items: center; gap: 12px;
    font-family: "Oswald", "Arial Narrow", sans-serif; font-weight: 700;
    font-size: 34px; color: var(--white); letter-spacing: 0.5px;
  }
  .phone__icon { width: 44px; height: 36px; }
  .brand {
    position: absolute; left: 192px; top: 140px; width: 388px; height: 200px;
    display: flex; align-items: center; justify-content: center; text-align: center;
    font-size: 40px; line-height: 1.2; color: var(--white); font-weight: 400; padding: 0 20px;
  }
  .headline {
    position: absolute; left: 0; top: 366px; width: 851px; text-align: center;
    font-size: 32px; font-weight: 700; color: var(--ink);
  }
  .transmitter {
    position: absolute; left: 60px; top: 414px; width: 731px; text-align: center;
    font-size: 19px; line-height: 1.35; color: var(--ink);
  }
  .transmitter strong { color: var(--red-dark); }
  .services-title {
    position: absolute; left: 160px; top: 568px;
    font-size: 44px; color: var(--white); font-weight: 400;
  }
  .service-list { position: absolute; left: 68px; top: 684px; list-style: none; }
  .service-list li {
    position: relative; padding-left: 39px;
    font-size: 32px; line-height: 44px; color: var(--ink);
  }
  .service-list li.wrap { width: 440px; }
  .service-list li::before {
    content: ""; position: absolute; left: 0; top: 7px; width: 30px; height: 30px;
    border-radius: 50%; border: 2px solid var(--red); background: var(--white);
  }
  .service-list li::after {
    content: ""; position: absolute; left: 7px; top: 15px; width: 10px; height: 10px;
    border-top: 4px solid var(--red); border-right: 4px solid var(--red);
    transform: rotate(45deg);
  }
  .price {
    position: absolute; right: 30px; top: 1126px;
    font-family: "Oswald", "Arial Narrow", sans-serif; font-weight: 700;
    font-size: 40px; color: var(--white);
    text-shadow: 2px 2px 0 #3a0004, -1px -1px 0 #3a0004, 1px -1px 0 #3a0004, -1px 1px 0 #3a0004;
  }
</style>
</head>
<body>
<main class="flyer">
  <svg class="flyer__shapes" width="851" height="1200" viewBox="0 0 851 1200" xmlns="http://www.w3.org/2000/svg">
    <defs>
      <linearGradient id="photoTone" x1="0" y1="0" x2="0" y2="1">
        <stop offset="0" stop-color="#d8d8d8"/>
        <stop offset="0.55" stop-color="#b9b9b9"/>
        <stop offset="1" stop-color="#d8d8d8"/>
      </linearGradient>
      <linearGradient id="cinemaTone" x1="0" y1="0" x2="0" y2="1">
        <stop offset="0" stop-color="#2c3140"/>
        <stop offset="0.45" stop-color="#4a4658"/>
        <stop offset="1" stop-color="#3a2c22"/>
      </linearGradient>
      <linearGradient id="redBand" x1="0" y1="0" x2="0" y2="1">
        <stop offset="0" stop-color="#ff3b3b"/>
        <stop offset="0.5" stop-color="#e3000f"/>
        <stop offset="1" stop-color="#a8000b"/>
      </linearGradient>
      <linearGradient id="silverLine" x1="0" y1="0" x2="0" y2="1">
        <stop offset="0" stop-color="#ffffff"/>
        <stop offset="1" stop-color="#8c8c8c"/>
      </linearGradient>
    </defs>

    <rect class="panel" x="0" y="0" width="851" height="1200" fill="#f4f4f4"/>

    <path class="showcase-photo" role="img" aria-label="Modern flat-screen TV on a glass shelf against a silver patterned feature wall"
          d="M0 70 H851 V760 Q560 500 0 513 Z" fill="url(#photoTone)"/>
    <rect class="showcase-screen" role="img" aria-label="TV screen showing the company name" x="192" y="140" width="388" height="200" fill="#4a4a4a" opacity="0.75"/>

    <path class="swoosh" d="M0 513 Q560 500 851 760 V800 Q560 540 0 522 Z" fill="url(#redBand)"/>

    <path class="services-pill" d="M180 557 H560 Q650 580 700 610 L660 630 H180 A36.5 36.5 0 0 1 180 557 Z" fill="url(#redBand)"/>

    <path class="topbar-line" d="M0 84 H530 L585 50 H851 V58 H590 L535 92 H0 Z" fill="url(#silverLine)"/>
    <path class="topbar" d="M0 0 H851 V50 H585 L530 84 H0 Z" fill="url(#redBand)"/>

    <rect class="cinema-frame" x="526" y="780" width="280" height="254" rx="22" fill="#e3000f"/>
    <rect class="cinema-photo" role="img" aria-label="Home cinema room with projector screen and rows of recliner seats" x="533" y="787" width="266" height="240" rx="17" fill="url(#cinemaTone)"/>

    <path class="footer-line" d="M0 1150 H380 L420 1104 H851 V1112 H424 L384 1158 H0 Z" fill="url(#silverLine)"/>
    <path class="footer" d="M0 1160 H386 L426 1114 H851 V1200 H0 Z" fill="url(#redBand)"/>
  </svg>

  <div class="phone">
    <svg class="phone__icon" viewBox="0 0 44 36" aria-hidden="true">
      <path d="M4 12 Q22 0 40 12 L36 18 L30 15 L30 10 Q22 7 14 10 L14 15 L8 18 Z" fill="#1a1a1a"/>
      <path d="M12 17 H32 L38 33 H6 Z" fill="#1a1a1a"/>
      <circle cx="22" cy="25" r="5" fill="#555"/>
    </svg>
    <span>0452 736 205</span>
  </div>

  <p class="brand">Clearpeak TV &amp; Aerial Svcs</p>

  <h1 class="headline">Poor TV reception… now a thing of the past!</h1>
  <p class="transmitter">Did you know a new transmitter has recently been installed in your area? We can therefore now <strong>GUARANTEE 100% PERFECT PICTURE.</strong></p>

  <h2 class="services-title">Our Services</h2>

  <ul class="service-list">
    <li>New Installs.</li>
    <li>Extra Outlets &amp; repairs.</li>
    <li class="wrap">TV wall mounting/Home Cinema.</li>
    <li>Pull down tall masts.</li>
    <li>Free 5 year warranty.</li>
    <li>Free signal testing.</li>
    <li>Free Onsite Quote.</li>
  </ul>

  <p class="price">Charges from only $95</p>
</main>
</body>
</html>
```